BRW Trifold Brochure

Would like a Trifold Brochure to use for marketing purposes. The company, Bright Ridge Works is a Handyman Service that offers Residential Home Repairs, Commercial Repairs, Drain Cleaning, Carpet Cleaning and Water Extraction.

I am attaching some pdf files to use as potential verbage and a copy of our business card and logo image file.

Would like to portray a professional image that sets us apart from a "mom and pops" type handyman service.

Industry/Entity Type

Marketing

```html
<!DOCTYPE html>
<html lang="en">
<head>
<meta charset="utf-8">
<title>Bright Ridge Works Trifold Brochure</title>
<link href="https://fonts.googleapis.com/css2?family=Yanone+Kaffeesatz:wght@600;700&family=Questrial&display=swap" rel="stylesheet">
<style>
  :root {
    --navy: #0d2243;
    --navy-deep: #0a1b36;
    --sky: #5aaee3;
    --sky-light: #6bb9ea;
    --blue: #2f86d2;
    --blue-deep: #1560b8;
    --ink: #0b1f3d;
    --white: #ffffff;
    --pale: #e6f2e8;
    --rule: rgba(255,255,255,0.35);
  }
  * { margin: 0; padding: 0; box-sizing: border-box; }
  html, body { width: 1200px; height: 857px; overflow: hidden; background: #eeeeee; }
  .brochure { position: relative; width: 1200px; height: 857px; overflow: hidden; font-family: "Questrial", sans-serif; }
  .panel { position: absolute; top: 0; height: 857px; width: 400px; }
  .panel-left { left: 0; background: linear-gradient(90deg, var(--sky-light), var(--sky)); }
  .panel-middle { left: 400px; background: linear-gradient(90deg, var(--sky), var(--blue)); }
  .panel-right { left: 800px; background: linear-gradient(90deg, var(--blue), var(--blue-deep)); }
  .left-navy { position: absolute; left: 0; top: 93px; width: 400px; height: 445px; background: var(--navy); }
  .middle-navy { position: absolute; left: 0; top: 0; width: 400px; height: 538px; background: var(--navy); }
  .divider { position: absolute; width: 1px; background: var(--rule); }
  .heading { font-family: "Yanone Kaffeesatz", sans-serif; font-weight: 700; color: var(--ink); }
  .call-us { position: absolute; left: 0; top: 10px; width: 400px; text-align: center; font-size: 32px; line-height: 37px; }
  .intro { position: absolute; left: 24px; top: 124px; width: 350px; color: var(--white); font-size: 16.4px; line-height: 25.8px; text-align: justify; }
  .thumb { position: absolute; top: 473px; width: 150px; height: 150px; border-radius: 50%; border: 3px solid var(--white); }
  .thumb-drafting { left: 32px; background: radial-gradient(circle at 40% 45%, #d6b48c, #8a6a4a); }
  .thumb-tools { left: 217px; background: radial-gradient(circle at 50% 50%, #b38a5c, #6e4f33); }
  .tagline { position: absolute; left: 0; top: 654px; width: 400px; text-align: center; font-size: 29px; line-height: 34px; font-weight: 600; }
  .website { position: absolute; left: 0; top: 792px; width: 400px; text-align: center; color: var(--white); font-size: 33px; letter-spacing: 0.5px; }
  .photo { position: absolute; left: 0; top: 0; }
  .promise { position: absolute; left: 424px; top: 560px; font-size: 29px; line-height: 34px; font-weight: 600; }
  .brand { position: absolute; font-family: "Yanone Kaffeesatz", sans-serif; font-weight: 700; color: var(--navy-deep); white-space: nowrap; }
  .brand-middle { left: 424px; top: 648px; font-size: 44px; }
  .brand-right { left: 800px; width: 400px; text-align: center; top: 720px; font-size: 56px; }
  .contact { position: absolute; left: 424px; top: 737px; font-family: "Yanone Kaffeesatz", sans-serif; font-weight: 600; color: var(--ink); font-size: 21px; line-height: 25px; list-style: none; }
  .contact li { display: flex; align-items: center; }
  .contact .icon { width: 22px; display: inline-flex; justify-content: flex-start; }
</style>
</head>
<body>
<main class="brochure">
  <section class="panel panel-left">
    <div class="left-navy"></div>
    <h2 class="heading call-us">Call Us Today !!!<br>(555) 014 - 2290</h2>
    <p class="intro">Bright Ridge Works is the answer to your home repair needs. Our staff of experienced technicians have the skills necessary to resolve all of your repair and maintenance issues. Minor Electrical, Plumbing, Heating and Air Conditioning. Honey Do Lists, Painting, Drywall Repair, Locks, Doors, Screens and Windows. Exterior Clean Up, Deck and Siding Repair. Appliance Repairs, Caulking, Tile...you name it we've got you covered Call Us Today to see how we can help you!!!</p>
    <div class="thumb thumb-drafting" role="img" aria-label="Photo of hands measuring and marking wood with a pencil"></div>
    <div class="thumb thumb-tools" role="img" aria-label="Photo of hand tools on a wooden workbench"></div>
    <p class="heading tagline">Bright Ridge Works<br>Handyman Services,<br>When you just need<br>to get it done!!!</p>
    <p class="website">www.BRW.com</p>
  </section>

  <section class="panel panel-middle">
    <div class="middle-navy"></div>
  </section>

  <section class="panel panel-right"></section>

  <div class="divider" style="left:400px; top:93px; height:764px;"></div>
  <div class="divider" style="left:800px; top:620px; height:237px;"></div>

  <svg class="photo" width="1200" height="857" viewBox="0 0 1200 857" role="img" aria-label="Photo of a handyman in overalls and work gloves wearing a tool belt in a bright kitchen">
    <defs>
      <linearGradient id="photoTone" x1="0" y1="0" x2="1" y2="0">
        <stop offset="0" stop-color="#d9b24a"/>
        <stop offset="0.4" stop-color="#e8e4b8"/>
        <stop offset="0.7" stop-color="#c9a55c"/>
        <stop offset="1" stop-color="#223a6a"/>
      </linearGradient>
    </defs>
    <path d="M504,0 H1200 V538 C1120,610 1030,645 930,640 C820,634 720,600 640,540 C540,460 480,330 480,200 C480,120 490,50 504,0 Z" fill="url(#photoTone)" stroke="var(--pale)" stroke-width="6"/>
  </svg>

  <h3 class="heading promise">Service you can<br>count on!!!</h3>
  <div class="brand brand-middle">Bright Ridge Works</div>
  <ul class="contact">
    <li><span class="icon"><svg width="12" height="17" viewBox="0 0 12 17"><path d="M6 0C2.7 0 0 2.6 0 5.8 0 10 6 17 6 17s6-7 6-11.2C12 2.6 9.3 0 6 0zm0 8.3A2.5 2.5 0 1 1 6 3.3a2.5 2.5 0 0 1 0 5z" fill="var(--ink)"/></svg></span>2719 Harbor Lane</li>
    <li><span class="icon"></span>Maple Grove, KS 66990</li>
    <li><span class="icon">@</span>info@BrightRidgeWorks.com</li>
    <li><span class="icon"><svg width="16" height="16" viewBox="0 0 16 16"><circle cx="8" cy="8" r="7" fill="none" stroke="var(--ink)" stroke-width="1.4"/><path d="M5.5 4.2l1.4 1.6-.8 1c.5 1.1 1.3 1.9 2.3 2.4l1-.8 1.6 1.4-.9 1.4C7.6 11 5 8.4 4.3 5.1z" fill="var(--ink)"/></svg></span>(555) 014 - 2290</li>
  </ul>

  <div class="brand brand-right">Bright Ridge Works</div>
</main>
</body>
</html>
```